Website Design for Agency

We require a website for our new agency. We have created a brief with our content, copywriting and most graphical assets. We just need some great with layout and to add some flair.
Updates

Went on vacation/holiday

Number of Pages Required

1 page

Font styles to use
Sans Serif

```html
<!DOCTYPE html>
<html lang="en">
<head>
<meta charset="utf-8">
<title>StoryProof Studio – Website Pages</title>
<link href="https://fonts.googleapis.com/css2?family=Barlow+Condensed:wght@500;600;700&family=Roboto:wght@400;500;700&display=swap" rel="stylesheet">
<style>
:root{
  --bg:#e3e3e5;
  --navy:#221f5e;
  --ink:#141414;
  --text:#3a3a3a;
  --muted:#6b6b6b;
  --line:#d9d9de;
  --soft:#f3f3f6;
  --art-a:#f4f4f6;
  --art-b:#e4e4ea;
  --photo-a:#5d6470;
  --photo-b:#8a9099;
  --green-a:#2f5b4b;
  --green-b:#6f7d7a;
}
*{box-sizing:border-box;margin:0;padding:0}
html,body{width:1200px;height:2769px;overflow:hidden}
body{background:var(--bg);font-family:'Roboto',sans-serif;color:var(--text);position:relative}
.panel{position:absolute;background:#fff;overflow:hidden}
.a{position:absolute}
.nav{position:absolute;left:0;top:0;width:100%;height:34px;box-shadow:0 2px 3px rgba(0,0,0,.08);display:flex;align-items:center;padding:0 16px 0 44px;background:#fff}
.nav .brand{font:600 13px 'Barlow Condensed',sans-serif;color:var(--ink);margin-right:14px;white-space:nowrap}
.nav .links{display:flex;gap:9px;font-size:6.4px;color:var(--ink);white-space:nowrap}
.nav .login{margin-left:auto;border:1px solid var(--navy);border-radius:10px;font-size:6.4px;padding:4px 14px;color:var(--navy)}
.nav .plans{margin-left:7px;background:var(--navy);border-radius:10px;font-size:6.4px;padding:5px 10px;color:#fff;white-space:nowrap}
.h-hero{font:600 22px/1.1 'Barlow Condensed',sans-serif;color:var(--ink);text-transform:uppercase}
.h-sec{font:600 14px/1.2 'Barlow Condensed',sans-serif;color:var(--ink);text-transform:uppercase;border-left:1.5px solid var(--ink);padding-left:7px}
.h-center{font:600 12px 'Barlow Condensed',sans-serif;color:var(--ink);text-transform:uppercase;text-align:center}
.p{font-size:5.8px;line-height:1.85;color:var(--text)}
.btn{display:inline-block;background:var(--navy);color:#fff;font-size:6px;padding:5px 12px;border-radius:12px;white-space:nowrap}
.btn-o{display:inline-block;border:1px solid var(--navy);color:var(--navy);font-size:6px;padding:4px 11px;border-radius:12px;margin-left:8px;background:#fff;white-space:nowrap}
.art{background:linear-gradient(140deg,var(--art-a),var(--art-b));box-shadow:0 2px 8px rgba(0,0,0,.12)}
.art-flat{background:linear-gradient(140deg,var(--art-a),var(--art-b))}
.logos{display:flex;align-items:center;gap:16px;font:600 8px 'Barlow Condensed',sans-serif;color:#333;white-space:nowrap}
.logos .lead{font:500 5px/1.3 'Roboto',sans-serif;width:58px;white-space:normal}
.brand-big{font:700 26px 'Barlow Condensed',sans-serif;color:var(--ink);text-align:center;width:100%}
.contacts{display:flex;justify-content:space-between;width:100%}
.contact{display:flex;gap:6px;align-items:flex-start;font-size:5px;line-height:1.5;color:var(--text)}
.contact b{display:block;font-weight:500;font-size:4.6px;color:var(--ink)}
.contact svg{flex:none}
.footer{position:absolute;left:0;width:100%;height:31px;background:var(--navy);display:flex;justify-content:center;align-items:center;gap:17px;font-size:6px;color:#fff}
.copy{position:absolute;left:0;width:100%;text-align:center;font-size:5.6px;color:var(--ink)}
.checks{display:flex;justify-content:space-between}
.check{display:flex;gap:5px;font-size:5.6px;line-height:1.4;color:var(--text);width:118px}
.check svg{flex:none}
.step{position:absolute;width:150px;border:1px solid var(--line);border-radius:6px;padding:10px 8px;background:#fff}
.step .ico{width:30px;height:30px;border:1.5px solid var(--ink);border-radius:4px;position:relative;flex:none}
.step .head{display:flex;align-items:center;gap:12px;margin-bottom:9px}
.step .title{font:500 11px/1.2 'Roboto',sans-serif;color:var(--ink)}
.step .p{font-size:4.8px;line-height:1.75}
.bul{display:flex;gap:5px;font-size:6px;line-height:1.45;color:var(--navy);margin-bottom:8px}
.bul svg{flex:none;margin-top:1px}
.cat{position:absolute;left:46px;width:462px;height:148px;border:1px solid var(--line);border-radius:4px;padding:8px 8px}
.cat h3{font:500 8px 'Roboto',sans-serif;color:var(--ink);text-transform:uppercase}
.cat .d{font-size:4.6px;color:var(--text);margin-top:3px;height:12px}
.thumbs{display:flex;gap:10px;margin-top:4px}
.thumb{width:104px;height:92px;position:relative;background:linear-gradient(135deg,var(--photo-a),var(--photo-b))}
.thumb.green{background:linear-gradient(135deg,var(--green-a),var(--green-b))}
.thumb .play{position:absolute;left:6px;bottom:6px;width:11px;height:11px;border-radius:50%;background:#111;display:flex;align-items:center;justify-content:center}
.price{position:absolute;top:2278px;width:140px;height:220px;background:#fff;border:1px solid var(--line);text-align:center;padding-top:22px}
.price.feat{background:var(--navy);color:#fff;border-color:var(--navy);width:152px;height:226px;top:2272px}
.price .name{font:500 9px 'Roboto',sans-serif;letter-spacing:.3px;color:var(--navy)}
.price.feat .name{color:#fff}
.price .amt{font:700 15px 'Roboto',sans-serif;margin-top:10px;color:var(--ink)}
.price.feat .amt{color:#fff}
.price .per{font-size:7px;color:var(--muted);margin-top:6px}
.price.feat .per{color:#ddd}
.price .lorem{font-size:6.2px;line-height:1.95;color:var(--muted);margin:22px 14px 0}
.price.feat .lorem{color:#fff}
.price .pb{display:inline-block;margin-top:14px;background:var(--navy);color:#fff;font-size:6px;padding:5px 12px;border-radius:12px}
.price.feat .pb{background:#fff;color:var(--navy)}
.ul li{list-style:none;display:flex;gap:6px;font-size:6.2px;line-height:1.7;color:var(--text);margin-bottom:4px}
.sq{width:6px;height:6px;background:var(--ink);flex:none;margin-top:2px}
</style>
</head>
<body>

<!-- ===== Home page ===== -->
<section class="panel" style="left:28px;top:32px;width:552px;height:2694px">
  <nav class="nav">
    <span class="brand">StoryProof Studio</span>
    <span class="links"><span>Home</span><span>Services</span><span>How it works</span><span>Examples</span><span>Contact</span></span>
    <span class="login">Login</span><span class="plans">Plans &amp; Pricing</span>
  </nav>

  <h1 class="a h-hero" style="left:44px;top:104px">Win more hearts with<br><span style="font-size:26px">powerful case studies</span></h1>
  <p class="a p" style="left:44px;top:166px;width:240px">Testimonial Videos, written PDFs, slides, one-pagers and social media content. We create spellbinding case study stories and videos that will drive business for your revenue team. No more writing, proofing organizing videographers and time-consuming hassles. We'll handle everything 100% and deliver to you powerful marketing assets you'll be proud to share.</p>
  <div class="a" style="left:0;top:250px;width:44px;height:1px;background:var(--ink)"></div>
  <svg class="a" style="left:42px;top:238px" width="24" height="24" viewBox="0 0 24 24"><circle cx="12" cy="12" r="11" fill="var(--navy)"/><path d="M10 8l6 4-6 4z" fill="#fff"/></svg>
  <span class="a btn-o" style="left:74px;top:243px;margin:0;padding:4px 14px">Learn more</span>
  <div class="a art-flat" style="left:312px;top:72px;width:226px;height:200px;border-radius:2px" role="img" aria-label="Line illustration of a person riding a rising arrow chart"></div>

  <div class="a logos" style="left:48px;top:354px">
    <span class="lead">Trusted by hundreds of top companies</span>
    <span>Northwave</span><span>Kelvar</span><span>Medrona</span><span>Carewell</span><span>Harbor Capital</span><span>Stridewear</span><span>Petrolux</span>
  </div>

  <div class="a art" style="left:45px;top:410px;width:212px;height:175px" role="img" aria-label="Illustration of a person working at a laptop surrounded by icons"></div>
  <h2 class="a h-sec" style="left:290px;top:426px;width:230px">Capture results, built trust and win new business</h2>
  <p class="a p" style="left:298px;top:474px;width:218px">Combining real-world results with social proof, one well-produced customer story with multiple marketing assets will do a LOT of the heavy lifting for your business sales...because it comes directly from the mouth of a happy human who loves what you do.</p>
  <span class="a btn" style="left:294px;top:530px">Learn more</span>

  <div class="a art-flat" style="left:288px;top:605px;width:232px;height:212px" role="img" aria-label="Collage of case study PDF pages, slides and social posts"></div>
  <h2 class="a h-sec" style="left:45px;top:676px;width:232px">Don't settle for just a single case study. Get a lot more.</h2>
  <p class="a p" style="left:53px;top:718px;width:220px">Narrative stories with your customer as the hero is key to readability and persuasion. Get professionally wordsmithed case studies to upload to your website, social channels, and move with pride.</p>
  <div class="a" style="left:48px;top:771px"><span class="btn">Learn more</span><span class="btn-o">Plans and Pricing</span></div>

  <div class="a art" style="left:45px;top:866px;width:212px;height:175px;background:#fff">
    <svg width="212" height="175" viewBox="0 0 212 175"><rect x="22" y="18" width="168" height="140" rx="10" fill="#3a3a3a"/><circle cx="36" cy="34" r="3" fill="#e8564b"/><circle cx="46" cy="34" r="3" fill="#f1b440"/><circle cx="56" cy="34" r="3" fill="#5cc15a"/><circle cx="106" cy="87" r="20" fill="#fff"/><path d="M100 77l16 10-16 10z" fill="#3a3a3a"/><rect x="32" y="138" width="148" height="9" rx="2" fill="#1e1e1e"/><rect x="56" y="141" width="100" height="3" fill="#fff"/><path d="M38 140l4 2.5-4 2.5z" fill="#fff"/></svg>
  </div>
  <h2 class="a h-sec" style="left:290px;top:882px;width:210px">Get a testimonial video anywhere nationwide</h2>
  <p class="a p" style="left:298px;top:924px;width:220px">You get our team of pros to handle the outreach, the interviews, the field production (or remote) and all the editing, graphics and storytelling for a lot less than you think. Powerful, proven content that moves the needle.</p>
  <div class="a" style="left:294px;top:992px"><span class="btn">Learn more</span><span class="btn-o">Plans and Pricing</span></div>

  <div class="a art" style="left:278px;top:1075px;width:212px;height:175px" role="img" aria-label="Green sales collateral sheets and brochure pages"></div>
  <h2 class="a h-sec" style="left:45px;top:1112px">Promo &amp; sales collateral</h2>
  <p class="a p" style="left:53px;top:1144px;width:222px">From one-sheets, slides, long, short, and ultra-short articles for your website, blog, or sales team. You are in good hands knowing the content you get back is marketing gold. All without the headaches.</p>
  <span class="a btn" style="left:48px;top:1194px">Learn more</span>

  <div class="a art" style="left:45px;top:1310px;width:212px;height:175px" role="img" aria-label="Illustration of a person on a laptop with floating documents"></div>
  <h2 class="a h-sec" style="left:290px;top:1340px">It's more than marketing</h2>
  <p class="a p" style="left:298px;top:1366px;width:218px">No more awful sales sheets and dull corporate announcements that tell people to spend their money without reason. Our team of Laurel Award-winning journalists ensure your case studies are authentic. They're real. They're raw. They give people a reason to trust you, and, more importantly, a reason to give you their business.</p>
  <span class="a btn" style="left:294px;top:1436px">Learn more</span>

  <div class="a art" style="left:290px;top:1540px;width:212px;height:175px" role="img" aria-label="Illustration of a team collaborating around a whiteboard"></div>
  <h2 class="a h-sec" style="left:42px;top:1570px;width:225px">Need help promoting your customer story? We got you.</h2>
  <p class="a p" style="left:47px;top:1614px;width:225px">You get campaign level help from our team. Landing pages, lead capture forms, press releases &amp; PR outreach to 400+ organizations and 100,000 journalists. All done by former our in-house former reporters who know how it's done.</p>
  <span class="a btn" style="left:48px;top:1672px">Learn more</span>

  <p class="a" style="left:0;top:1762px;width:552px;text-align:center;font:600 19px/1.2 'Barlow Condensed',sans-serif;color:var(--ink)">100% Stress-Free Case Study<br>Project Management</p>

  <div class="a art-flat" style="left:88px;top:1842px;width:140px;height:125px" role="img" aria-label="Illustration of a person relaxing under a palm tree"></div>
  <div class="a" style="left:245px;top:1850px;width:290px;height:34px;background:var(--soft)"></div>
  <h2 class="a h-sec" style="left:290px;top:1858px;font-size:17px">Get more for less</h2>
  <p class="a" style="left:290px;top:1898px;width:222px;font-size:6.6px;line-height:1.95;text-align:justify">Whether you manage the marketing yourself or or have an in-house marketing manager, getting case studies done can be time consuming and costly if you don't do it right. We believe partnering with a case study expert can help your business prosper and establish itself as an industry leader.</p>

  <div class="a" style="left:42px;top:2022px;width:305px;height:34px;background:var(--soft)"></div>
  <h2 class="a" style="left:42px;top:2028px;font:500 17px 'Roboto',sans-serif;color:var(--ink);border-left:1.5px solid var(--ink);padding-left:4px;text-transform:none">Free Up Your Schedule</h2>
  <p class="a" style="left:46px;top:2060px;width:250px;font-size:6.4px;line-height:1.8">Our team of experienced video producers and content creators use proven persuasion strategies to create attention-grabbing case studies.</p>
  <ul class="a ul" style="left:46px;top:2086px;width:250px">
    <li><span class="sq"></span>We provide respectful and proactive client management throughout each case study project.</li>
    <li><span class="sq"></span>We produce quality assets that your client will love and protect your brand's reputation.</li>
    <li><span class="sq"></span>We save you countless hours of time and effort.</li>
    <li><span class="sq"></span>We ensure your satisfaction with every piece of case study material we deliver.</li>
  </ul>
  <div class="a art-flat" style="left:355px;top:2012px;width:180px;height:130px" role="img" aria-label="Illustration of two people reviewing a checklist board"></div>

  <div class="a" style="left:0;top:2170px;width:552px;height:330px;background:linear-gradient(180deg,#fff 0%,#f6f3f8 40%,#fbf0f5 70%,#fff 100%)" role="img" aria-label="Soft pink low-poly background"></div>
  <div class="price" style="left:42px"><div class="name">STORYPROOF STUDIO</div><div class="amt">$7.95</div><div class="per">per user/per month</div><p class="lorem">Lorem ipsum dolor sit amet, consectetur adipiscing elit, sed do eiusmod tempor incididunt ut labore et dolore magna aliqua.</p><span class="pb">Plans &amp; Pricing</span></div>
  <div class="price feat" style="left:198px"><div class="name">STORYPROOF STUDIO</div><div class="amt">$7.95</div><div class="per">per user/per month</div><p class="lorem">Lorem ipsum dolor sit amet, consectetur adipiscing elit, sed do eiusmod tempor incididunt ut labore et dolore magna aliqua.</p><span class="pb">Plans &amp; Pricing</span></div>
  <div class="price" style="left:365px"><div class="name">STORYPROOF STUDIO</div><div class="amt">$7.95</div><div class="per">per user/per month</div><p class="lorem">Lorem ipsum dolor sit amet, consectetur adipiscing elit, sed do eiusmod tempor incididunt ut labore et dolore magna aliqua.</p><span class="pb">Plans &amp; Pricing</span></div>

  <div class="a brand-big" style="left:0;top:2540px;width:552px">StoryProof Studio</div>
  <div class="a contacts" style="left:55px;top:2597px;width:400px">
    <div class="contact"><svg width="14" height="14" viewBox="0 0 14 14"><circle cx="7" cy="7" r="7" fill="#111"/><rect x="3.6" y="4.6" width="6.8" height="4.8" fill="none" stroke="#fff" stroke-width=".8"/><path d="M3.6 4.6L7 7.3 10.4 4.6" fill="none" stroke="#fff" stroke-width=".8"/></svg><span><b>EMAIL</b>hello@storyproof.example</span></div>
    <div class="contact"><svg width="14" height="14" viewBox="0 0 14 14"><circle cx="7" cy="7" r="7" fill="#111"/><path d="M7 3.5a2.3 2.3 0 0 1 2.3 2.3C9.3 7.6 7 10.5 7 10.5S4.7 7.6 4.7 5.8A2.3 2.3 0 0 1 7 3.5z" fill="#fff"/><circle cx="7" cy="5.8" r=".9" fill="#111"/></svg><span><b>OUR LOCATION</b>19 Nemo enim ipsam voluptatem<br>quia voluptas sit</span></div>
    <div class="contact"><svg width="14" height="14" viewBox="0 0 14 14"><circle cx="7" cy="7" r="7" fill="#111"/><path d="M4.6 4c.4-.3.9-.3 1.1.1l.6 1.1c.2.4 0 .7-.3 1 .4.9 1 1.5 1.9 1.9.3-.3.6-.5 1-.3l1.1.6c.4.2.4.7.1 1.1-.6.7-1.5.8-2.3.4C6.3 9.2 4.8 7.7 4.2 6.3c-.4-.8-.3-1.7.4-2.3z" fill="#fff"/></svg><span><b>PHONE NUMBER</b>+1 555-010-0199</span></div>
  </div>
  <div class="footer" style="top:2623px"><span>Home</span><span>Services</span><span>How it works</span><span>Examples Contact</span></div>
  <p class="copy" style="top:2673px">Copyright © 2022 StoryProof Studio - All Rights Reserved.</p>
</section>

<!-- ===== How it works page ===== -->
<section class="panel" style="left:617px;top:32px;width:552px;height:1312px">
  <nav class="nav">
    <span class="brand">StoryProof Studio</span>
    <span class="links"><span>Home</span><span>Services</span><span>How it works</span><span>Examples</span><span>Contact</span></span>
    <span class="login">Login</span><span class="plans">Plans &amp; Pricing</span>
  </nav>
  <h1 class="a h-hero" style="left:47px;top:66px">How it works</h1>
  <p class="a p" style="left:47px;top:98px;width:158px;font-size:5.4px;line-height:1.95;color:var(--ink)">We get it. The idea of planning and producing testimonial videos and written case studies may feel like a challenge. What should you ask? How can you get the best answer? How can you turn your notes into valuable content you can use across mediums and platforms?</p>
  <p class="a p" style="left:47px;top:178px;width:158px;font-size:5.4px;line-height:1.95;color:var(--ink)">Our case study team is made up of former business news journalists from Channel North, Metro Network and Wire Press. We handle the whole process for you—from interviews to writing, editing, filming and design! You choose how involved you want to be at any time.</p>
  <div class="a art-flat" style="left:290px;top:50px;width:250px;height:220px" role="img" aria-label="Illustration of a person writing on a laptop with floating notes"></div>

  <h2 class="a h-sec" style="left:165px;top:276px;font-size:13px">Every step managed for you</h2>
  <div class="a checks" style="left:53px;top:314px;width:455px">
    <div class="check"><svg width="8" height="8" viewBox="0 0 8 8"><circle cx="4" cy="4" r="4" fill="var(--navy)"/><path d="M2.2 4.1l1.2 1.2 2.4-2.5" fill="none" stroke="#fff" stroke-width=".9"/></svg>Initial strategy calls with you</div>
    <div class="check"><svg width="8" height="8" viewBox="0 0 8 8"><circle cx="4" cy="4" r="4" fill="var(--navy)"/><path d="M2.2 4.1l1.2 1.2 2.4-2.5" fill="none" stroke="#fff" stroke-width=".9"/></svg>Reaching out to your clients</div>
    <div class="check"><svg width="8" height="8" viewBox="0 0 8 8"><circle cx="4" cy="4" r="4" fill="var(--navy)"/><path d="M2.2 4.1l1.2 1.2 2.4-2.5" fill="none" stroke="#fff" stroke-width=".9"/></svg>Preparing and running client interviews</div>
    <div class="check" style="width:95px"><svg width="8" height="8" viewBox="0 0 8 8"><circle cx="4" cy="4" r="4" fill="var(--navy)"/><path d="M2.2 4.1l1.2 1.2 2.4-2.5" fill="none" stroke="#fff" stroke-width=".9"/></svg>Writing, producing cast study content</div>
  </div>

  <div class="step" style="left:47px;top:356px;height:172px"><div class="head"><div class="ico"></div><span class="title">Strategy Call</span></div><p class="p">We would initially send you a link to a form to fill out that offers some more info about the case study project for us. Then let's jump on a video call to discuss your project. We'll cover what you'd like to get done, what assets you would like, and decide on who your client(s) are including contact information. We can discuss why this client(s) love what you do, what successes/wins you have had with the client(s) and what messages you hope to capture from them.</p></div>
  <div class="step" style="left:203px;top:356px;height:172px"><div class="head"><div class="ico"></div><span class="title">Contact client(s)</span></div><p class="p">We often have you contact your own client(s) first to ask them about participating in a case study. We can provide you with an email template to use to make the request, including some information on what would be required for your client and what to expect. Once the clients have agreed, we take it from there. We'll arrange an interview day/time that works for your client.</p></div>
  <div class="step" style="left:360px;top:356px;height:172px"><div class="head"><div class="ico"></div><span class="title">Review and<br>Interview</span></div><p class="p">We will then conduct our research on your company, and the relevant product or service you offer to this client - and why they are happy. Using our expert charm and professionalism to disarm your client and make them feel comfortable, we interview them on camera (at their office or remotely) asking questions you helped develop. The interview usually lasts no more than 15-20 minutes.</p></div>
  <div class="step" style="left:47px;top:542px;height:150px"><div class="head"><div class="ico"></div><span class="title">Editing</span></div><p class="p">If you wish at this stage, we can share with you a link to the interview transcript. You can either highlight the points/quotes you want to include, or allow our team of experts to select for you. We will then edit the interview into a cohesive story.</p></div>
  <div class="step" style="left:203px;top:542px;height:150px"><div class="head"><div class="ico"></div><span class="title">Revisions</span></div><p class="p">Here you and your team will review our work, the initial version of the testimonial video and the written material (supplied in a doc for review). This will give you all the time you need to suggest revisions. While we add some graphics and titles and logos to the video, we will also get the design work done on the case study PDF and the social assets. Again, you can make unlimited revisions along the way.</p></div>
  <div class="step" style="left:360px;top:542px;height:150px"><div class="head"><div class="ico"></div><span class="title">Deliver Content</span></div><p class="p">You will get a link to download the approved video, case study and other assets to use for your business. If you require some additional services like press release writing and distribution, we will deliver this as well.</p></div>

  <h2 class="a h-sec" style="left:155px;top:752px;font-size:14px">Your new case study partner</h2>
  <div class="a art" style="left:0;top:820px;width:245px;height:190px" role="img" aria-label="Illustration of a developer surrounded by code symbols"></div>
  <p class="a" style="left:280px;top:795px;width:232px;font-size:6.2px;line-height:1.9;color:var(--muted)">Unlike many marketing services, our content generation and production experience is entirely suited to the purpose of customer success stories. You can rest assured we know how to convey complex information and identify the core message in each story.</p>
  <p class="a" style="left:280px;top:856px;width:210px;font-size:6.4px;line-height:1.8;color:var(--ink);font-weight:700">With over 25 years of journalism experience with some of the most reputable companies, including Channel North, Globe Broadcast, Maple News, and Lakeshore TV, we bring precious values to case study copywriting:</p>
  <div class="a" style="left:280px;top:916px;width:225px">
    <div class="bul"><svg width="7" height="7" viewBox="0 0 8 8"><circle cx="4" cy="4" r="3.4" fill="none" stroke="var(--navy)"/><path d="M2.4 4.1l1.1 1.1 2.2-2.3" fill="none" stroke="var(--navy)" stroke-width=".9"/></svg>How to make your customer feel great in the process, while protecting your company's reputation</div>
    <div class="bul"><svg width="7" height="7" viewBox="0 0 8 8"><circle cx="4" cy="4" r="3.4" fill="none" stroke="var(--navy)"/><path d="M2.4 4.1l1.1 1.1 2.2-2.3" fill="none" stroke="var(--navy)" stroke-width=".9"/></svg>A keen eye for valuable content</div>
    <div class="bul"><svg width="7" height="7" viewBox="0 0 8 8"><circle cx="4" cy="4" r="3.4" fill="none" stroke="var(--navy)"/><path d="M2.4 4.1l1.1 1.1 2.2-2.3" fill="none" stroke="var(--navy)" stroke-width=".9"/></svg>Interviewing experience and skills</div>
    <div class="bul"><svg width="7" height="7" viewBox="0 0 8 8"><circle cx="4" cy="4" r="3.4" fill="none" stroke="var(--navy)"/><path d="M2.4 4.1l1.1 1.1 2.2-2.3" fill="none" stroke="var(--navy)" stroke-width=".9"/></svg>How to capture the essence of every message</div>
    <div class="bul"><svg width="7" height="7" viewBox="0 0 8 8"><circle cx="4" cy="4" r="3.4" fill="none" stroke="var(--navy)"/><path d="M2.4 4.1l1.1 1.1 2.2-2.3" fill="none" stroke="var(--navy)" stroke-width=".9"/></svg>How to explain complex topics in an accessible manner in each content format</div>
  </div>

  <p class="a h-center" style="left:0;top:1052px;width:552px">We deliver high quality customer stories, period.</p>
  <p class="a" style="left:70px;top:1078px;width:412px;text-align:center;font-size:5.8px;line-height:1.95">Whether a client requests to film their testimonial remotely or whether we meet them on-site, we know all the tips, tricks, and strategies to deliver high-quality videos and edit them professionally. In other words, if your client chooses to record their testimonial remotely, we have the skills and experience to guide them through the process and produce professional results. If a client prefers to be recorded by our team, we are happy to meet them and bring the equipment on-site for a pain-less 30 minutes of their time. 08/12</p>
  <div class="a brand-big" style="left:0;top:1140px">StoryProof Studio</div>
  <div class="a contacts" style="left:57px;top:1212px;width:420px">
    <div class="contact"><svg width="14" height="14" viewBox="0 0 14 14"><circle cx="7" cy="7" r="7" fill="#111"/><rect x="3.6" y="4.6" width="6.8" height="4.8" fill="none" stroke="#fff" stroke-width=".8"/><path d="M3.6 4.6L7 7.3 10.4 4.6" fill="none" stroke="#fff" stroke-width=".8"/></svg><span><b>EMAIL</b>hello@storyproof.example</span></div>
    <div class="contact"><svg width="14" height="14" viewBox="0 0 14 14"><circle cx="7" cy="7" r="7" fill="#111"/><path d="M7 3.5a2.3 2.3 0 0 1 2.3 2.3C9.3 7.6 7 10.5 7 10.5S4.7 7.6 4.7 5.8A2.3 2.3 0 0 1 7 3.5z" fill="#fff"/><circle cx="7" cy="5.8" r=".9" fill="#111"/></svg><span><b>OUR LOCATION</b>19 Nemo enim ipsam voluptatem<br>quia voluptas sit</span></div>
    <div class="contact"><svg width="14" height="14" viewBox="0 0 14 14"><circle cx="7" cy="7" r="7" fill="#111"/><path d="M4.6 4c.4-.3.9-.3 1.1.1l.6 1.1c.2.4 0 .7-.3 1 .4.9 1 1.5 1.9 1.9.3-.3.6-.5 1-.3l1.1.6c.4.2.4.7.1 1.1-.6.7-1.5.8-2.3.4C6.3 9.2 4.8 7.7 4.2 6.3c-.4-.8-.3-1.7.4-2.3z" fill="#fff"/></svg><span><b>PHONE NUMBER</b>+1 555-010-0199</span></div>
  </div>
  <div class="footer" style="top:1245px"><span>Home</span><span>Services</span><span>How it works</span><span>Examples Contact</span></div>
  <p class="copy" style="top:1290px">Copyright © 2022 StoryProof Studio - All Rights Reserved.</p>
</section>

<!-- ===== Examples page ===== -->
<section class="panel" style="left:617px;top:1368px;width:552px;height:1347px">
  <nav class="nav">
    <span class="brand">StoryProof Studio</span>
    <span class="links"><span>Home</span><span>Services</span><span>How it works</span><span>Examples</span><span>Contact</span></span>
    <span class="login">Login</span><span class="plans">Plans &amp; Pricing</span>
  </nav>
  <h1 class="a h-hero" style="left:45px;top:62px">Examples of our work</h1>
  <p class="a" style="left:45px;top:94px;font-size:5.8px;font-weight:500;color:var(--ink)">Why settle for a single case study doc? We give you multiple assets all from the same customer story</p>

  <div class="cat" style="top:112px"><h3>On location video testimonials</h3><p class="d">Cinematic, high-powered video where our crew show up to your client's office or facility and put your customer in the spotlight.</p>
    <div class="thumbs">
      <div class="thumb" role="img" aria-label="Video still of an on-site business interview"><span class="play"><svg width="5" height="5" viewBox="0 0 5 5"><path d="M1 .5l3.5 2-3.5 2z" fill="#fff"/></svg></span></div>
      <div class="thumb" role="img" aria-label="Video still of an on-site business interview"><span class="play"><svg width="5" height="5" viewBox="0 0 5 5"><path d="M1 .5l3.5 2-3.5 2z" fill="#fff"/></svg></span></div>
      <div class="thumb" role="img" aria-label="Video still of an on-site business interview"><span class="play"><svg width="5" height="5" viewBox="0 0 5 5"><path d="M1 .5l3.5 2-3.5 2z" fill="#fff"/></svg></span></div>
      <div class="thumb" role="img" aria-label="Video still of an on-site business interview"><span class="play"><svg width="5" height="5" viewBox="0 0 5 5"><path d="M1 .5l3.5 2-3.5 2z" fill="#fff"/></svg></span></div>
    </div></div>

  <div class="cat" style="top:277px"><h3>Remote video testimonials</h3><p class="d">Get a polished production without setting foot in your customers' office. We use your clients smartphone (and a special app) to record great HD video.</p>
    <div class="thumbs">
      <div class="thumb" role="img" aria-label="Video still of a remote testimonial"><span class="play"><svg width="5" height="5" viewBox="0 0 5 5"><path d="M1 .5l3.5 2-3.5 2z" fill="#fff"/></svg></span></div>
      <div class="thumb" role="img" aria-label="Video still of a remote testimonial"><span class="play"><svg width="5" height="5" viewBox="0 0 5 5"><path d="M1 .5l3.5 2-3.5 2z" fill="#fff"/></svg></span></div>
      <div class="thumb" role="img" aria-label="Video still of a remote testimonial"><span class="play"><svg width="5" height="5" viewBox="0 0 5 5"><path d="M1 .5l3.5 2-3.5 2z" fill="#fff"/></svg></span></div>
      <div class="thumb" role="img" aria-label="Video still of a remote testimonial"><span class="play"><svg width="5" height="5" viewBox="0 0 5 5"><path d="M1 .5l3.5 2-3.5 2z" fill="#fff"/></svg></span></div>
    </div></div>

  <div class="cat" style="top:442px"><h3>Written case studies</h3><p class="d">Long, short, and ultra-short assets for your website, blog, or sales team.</p>
    <div class="thumbs">
      <div class="thumb green" role="img" aria-label="Preview of a green written case study"><span class="play"><svg width="5" height="5" viewBox="0 0 5 5"><path d="M1 .5l3.5 2-3.5 2z" fill="#fff"/></svg></span></div>
      <div class="thumb green" role="img" aria-label="Preview of a green written case study"><span class="play"><svg width="5" height="5" viewBox="0 0 5 5"><path d="M1 .5l3.5 2-3.5 2z" fill="#fff"/></svg></span></div>
      <div class="thumb green" role="img" aria-label="Preview of a green written case study"><span class="play"><svg width="5" height="5" viewBox="0 0 5 5"><path d="M1 .5l3.5 2-3.5 2z" fill="#fff"/></svg></span></div>
      <div class="thumb green" role="img" aria-label="Preview of a green written case study"><span class="play"><svg width="5" height="5" viewBox="0 0 5 5"><path d="M1 .5l3.5 2-3.5 2z" fill="#fff"/></svg></span></div>
    </div></div>

  <div class="cat" style="top:607px"><h3>Promo &amp; sales collateral</h3><p class="d">From one-sheets and slide decks to image quotes, audiograms, social media assets, and more.</p>
    <div class="thumbs">
      <div class="thumb green" role="img" aria-label="Preview of sales collateral sheet"><span class="play"><svg width="5" height="5" viewBox="0 0 5 5"><path d="M1 .5l3.5 2-3.5 2z" fill="#fff"/></svg></span></div>
      <div class="thumb green" role="img" aria-label="Preview of sales collateral sheet"><span class="play"><svg width="5" height="5" viewBox="0 0 5 5"><path d="M1 .5l3.5 2-3.5 2z" fill="#fff"/></svg></span></div>
      <div class="thumb green" role="img" aria-label="Preview of sales collateral sheet"><span class="play"><svg width="5" height="5" viewBox="0 0 5 5"><path d="M1 .5l3.5 2-3.5 2z" fill="#fff"/></svg></span></div>
      <div class="thumb green" role="img" aria-label="Preview of sales collateral sheet"><span class="play"><svg width="5" height="5" viewBox="0 0 5 5"><path d="M1 .5l3.5 2-3.5 2z" fill="#fff"/></svg></span></div>
    </div></div>

  <div class="cat" style="top:772px"><h3>Audiograms</h3><p class="d">Whether it's Snapline Stories, Chatter, Quipster or ProLink, audiograms are available in all shapes and sizes for reaching new listeners everywhere. These clips are typically extracted from the video!</p>
    <div class="thumbs">
      <div class="thumb green" role="img" aria-label="Preview of an audiogram clip"><span class="play"><svg width="5" height="5" viewBox="0 0 5 5"><path d="M1 .5l3.5 2-3.5 2z" fill="#fff"/></svg></span></div>
      <div class="thumb green" role="img" aria-label="Preview of an audiogram clip"><span class="play"><svg width="5" height="5" viewBox="0 0 5 5"><path d="M1 .5l3.5 2-3.5 2z" fill="#fff"/></svg></span></div>
      <div class="thumb green" role="img" aria-label="Preview of an audiogram clip"><span class="play"><svg width="5" height="5" viewBox="0 0 5 5"><path d="M1 .5l3.5 2-3.5 2z" fill="#fff"/></svg></span></div>
      <div class="thumb green" role="img" aria-label="Preview of an audiogram clip"><span class="play"><svg width="5" height="5" viewBox="0 0 5 5"><path d="M1 .5l3.5 2-3.5 2z" fill="#fff"/></svg></span></div>
    </div></div>

  <div class="cat" style="top:937px"><h3>Social, snackable content</h3><p class="d">We design more assets for you to use to actually drive revenue from social media.</p>
    <div class="thumbs">
      <div class="thumb green" role="img" aria-label="Preview of a social media post"><span class="play"><svg width="5" height="5" viewBox="0 0 5 5"><path d="M1 .5l3.5 2-3.5 2z" fill="#fff"/></svg></span></div>
      <div class="thumb green" role="img" aria-label="Preview of a social media post"><span class="play"><svg width="5" height="5" viewBox="0 0 5 5"><path d="M1 .5l3.5 2-3.5 2z" fill="#fff"/></svg></span></div>
      <div class="thumb green" role="img" aria-label="Preview of a social media post"><span class="play"><svg width="5" height="5" viewBox="0 0 5 5"><path d="M1 .5l3.5 2-3.5 2z" fill="#fff"/></svg></span></div>
      <div class="thumb green" role="img" aria-label="Preview of a social media post"><span class="play"><svg width="5" height="5" viewBox="0 0 5 5"><path d="M1 .5l3.5 2-3.5 2z" fill="#fff"/></svg></span></div>
    </div></div>

  <p class="a h-center" style="left:0;top:1106px;width:552px">We deliver high quality customer stories, period.</p>
  <p class="a" style="left:70px;top:1132px;width:412px;text-align:center;font-size:5.8px;line-height:1.95">Whether a client requests to film their testimonial remotely or whether we meet them on-site, we know all the tips, tricks, and strategies to deliver high-quality videos and edit them professionally. In other words, if your client chooses to record their testimonial remotely, we have the skills and experience to guide them through the process and produce professional results. If a client prefers to be recorded by our team, we are happy to meet them and bring the equipment on-site for a pain-less 30 minutes of their time. 08/12</p>
  <div class="a brand-big" style="left:0;top:1192px">StoryProof Studio</div>
  <div class="a contacts" style="left:57px;top:1258px;width:420px">
    <div class="contact"><svg width="14" height="14" viewBox="0 0 14 14"><circle cx="7" cy="7" r="7" fill="#111"/><rect x="3.6" y="4.6" width="6.8" height="4.8" fill="none" stroke="#fff" stroke-width=".8"/><path d="M3.6 4.6L7 7.3 10.4 4.6" fill="none" stroke="#fff" stroke-width=".8"/></svg><span><b>EMAIL</b>hello@storyproof.example</span></div>
    <div class="contact"><svg width="14" height="14" viewBox="0 0 14 14"><circle cx="7" cy="7" r="7" fill="#111"/><path d="M7 3.5a2.3 2.3 0 0 1 2.3 2.3C9.3 7.6 7 10.5 7 10.5S4.7 7.6 4.7 5.8A2.3 2.3 0 0 1 7 3.5z" fill="#fff"/><circle cx="7" cy="5.8" r=".9" fill="#111"/></svg><span><b>OUR LOCATION</b>19 Nemo enim ipsam voluptatem<br>quia voluptas sit</span></div>
    <div class="contact"><svg width="14" height="14" viewBox="0 0 14 14"><circle cx="7" cy="7" r="7" fill="#111"/><path d="M4.6 4c.4-.3.9-.3 1.1.1l.6 1.1c.2.4 0 .7-.3 1 .4.9 1 1.5 1.9 1.9.3-.3.6-.5 1-.3l1.1.6c.4.2.4.7.1 1.1-.6.7-1.5.8-2.3.4C6.3 9.2 4.8 7.7 4.2 6.3c-.4-.8-.3-1.7.4-2.3z" fill="#fff"/></svg><span><b>PHONE NUMBER</b>+1 555-010-0199</span></div>
  </div>
  <div class="footer" style="top:1293px"><span>Home</span><span>Services</span><span>How it works</span><span>Examples Contact</span></div>
  <p class="copy" style="top:1336px">Copyright © 2022 StoryProof Studio - All Rights Reserved.</p>
</section>

</body>
</html>
```